Business Card - Brisk Works
Stout Harbor BC
Project: Business Card - Brisk Works
Business Card - Brisk Works - Manufacturing
Creative Brief
Professional
Gordon Pratchett
gpratchett@stoutharbor-mail.com
"Build and Thrive"
emagineitgroup emagineitgroup
I accidentally erased #67, can it be put back on?
I like #105 as a start with the following changes: 1. the bottom portion of the card is black I would like this to be eliminated and center (2) shiny gold lines centered and measuring : TOP LINE - 2 6/8" AND THE BOTTOM LINE = 1 5/8" . These two lines should be centered . THE DISTANCE APART SHOULD BE 1/16". I would like for the two 'shiny gold lines' to be centered between the logo on top and my information below. I would also like for my name: GORDON PRATCHETT to be in bold black and all caps. I would like to see the rest of the info not in bold, but in black font. I would like the pareto chart (3) to the right on top of the black line to be completely eliminated. I only want to have a card that is one sided. I would also like to see the card as it is, currently, with the font in the black section on the lower half of the card, in white font.
Im liking the clear cards as well. Please give me more options on clear business cards that are perhaps not as generic.
glassfairy glassfairy
plz upload the logo file too
I have a current Business Card i would like to Add for an example. Please let me know where to add it.

```html
<!DOCTYPE html>
<html lang="en">
<head>
<meta charset="utf-8">
<title>Stout Harbor Business Card</title>
<link href="https://fonts.googleapis.com/css2?family=Exo+2:wght@400;500&display=swap" rel="stylesheet">
<style>
  :root {
    --bg: #e9e6e1;
    --card-white: #f6f6f6;
    --card-grey: #dcdcdc;
    --ink: #1f1f1f;
    --charcoal: #2b2b2b;
    --gold: #c6a25a;
    --gold-light: #e3cb8f;
    --text-light: #f2f2f2;
  }
  * { margin: 0; padding: 0; box-sizing: border-box; }
  html, body { width: 1200px; height: 899px; overflow: hidden; background: var(--bg); }
  .sheet {
    width: 1200px; height: 899px;
    display: flex; flex-direction: column; align-items: center; justify-content: center; gap: 40px;
  }
  .card {
    position: relative; width: 700px; height: 400px; overflow: hidden;
    background: radial-gradient(ellipse at 50% 35%, var(--card-white) 40%, var(--card-grey) 100%);
    box-shadow: 0 6px 18px rgba(0,0,0,.18);
    font-family: "Exo 2", sans-serif;
  }
  .card--back { height: 380px; width: 665px; }

  .brand { position: absolute; display: flex; align-items: center; gap: 14px; }
  .brand__mark { width: 34px; height: 34px; background: var(--ink); flex: none; }
  .brand__text { color: var(--ink); font-weight: 500; line-height: 1.15; white-space: nowrap; }
  .brand__name { font-size: 32px; letter-spacing: 1px; }
  .brand__tagline { font-size: 14px; letter-spacing: 3px; }
  .card--back .brand { left: 50%; top: 50%; transform: translate(-50%, -50%); }
  .card--front .brand { left: 48px; top: 60px; }
  .card--front .brand__name { font-size: 28px; }

  .swoosh { position: absolute; inset: 0; }
  .contacts { position: absolute; left: 48px; top: 252px; list-style: none; }
  .contacts li {
    display: flex; align-items: center; gap: 12px;
    color: var(--text-light); font-size: 15px; height: 27px;
  }
  .contacts svg { width: 16px; height: 16px; fill: var(--text-light); }
  .person { position: absolute; right: 52px; top: 176px; text-align: left; }
  .person__name { font-size: 26px; font-weight: 500; letter-spacing: 1px; color: var(--ink); }
  .person__title { font-size: 17px; color: var(--ink); margin-top: 2px; }
  .address { position: absolute; left: 440px; top: 300px; color: var(--text-light); font-size: 14px; line-height: 20px; }
  .website { position: absolute; left: 440px; top: 352px; color: var(--text-light); font-size: 16px; letter-spacing: .5px; }
</style>
</head>
<body>
<main class="sheet">
  <section class="card card--back" aria-label="Card back">
    <div class="brand">
      <span class="brand__mark" aria-hidden="true"></span>
      <div class="brand__text">
        <div class="brand__name">STOUT HARBOR, INC.</div>
        <div class="brand__tagline">BUILD AND THRIVE</div>
      </div>
    </div>
  </section>

  <section class="card card--front" aria-label="Card front">
    <svg class="swoosh" viewBox="0 0 700 400" preserveAspectRatio="none" aria-hidden="true">
      <path d="M0 205 C 160 180, 300 200, 420 255 C 500 290, 600 290, 700 280 L700 400 L0 400 Z" fill="var(--charcoal)"/>
      <path d="M0 205 C 160 180, 300 200, 420 255 C 500 290, 600 290, 700 280" fill="none" stroke="var(--gold)" stroke-width="5"/>
      <path d="M0 196 C 160 172, 300 190, 420 244 C 500 280, 600 282, 700 271" fill="none" stroke="var(--gold-light)" stroke-width="1.5"/>
    </svg>

    <div class="brand">
      <span class="brand__mark" aria-hidden="true"></span>
      <div class="brand__text">
        <div class="brand__name">STOUT HARBOR, INC.</div>
        <div class="brand__tagline">BUILD AND THRIVE</div>
      </div>
    </div>

    <div class="person">
      <div class="person__name">GORDON PRATCHETT</div>
      <div class="person__title">Managing Director</div>
    </div>

    <ul class="contacts">
      <li><svg viewBox="0 0 16 16"><path d="M3 1h3l1 4-2 1a9 9 0 0 0 5 5l1-2 4 1v3a2 2 0 0 1-2 2A13 13 0 0 1 1 3a2 2 0 0 1 2-2z"/></svg>012 555 0147</li>
      <li><svg viewBox="0 0 16 16"><path d="M5 0h6a1 1 0 0 1 1 1v14a1 1 0 0 1-1 1H5a1 1 0 0 1-1-1V1a1 1 0 0 1 1-1zm0 2v10h6V2z"/></svg>012 555 0147</li>
      <li><svg viewBox="0 0 16 16"><path d="M4 1h6l2 2v3h2v9H2V6h2zm1 1v4h6V3.5L9.5 2zM4 9v2h8V9z"/></svg>012 555 0147</li>
      <li><svg viewBox="0 0 16 16"><path d="M1 3h14v10H1zm1.5 1.2V12h11V4.2L8 8.5z"/></svg>gpratchett@stoutharbor-mail.com</li>
    </ul>

    <div class="address">214 Ninth Floor Pier<br>Harbor Road SHB</div>
    <div class="website">www.stoutharbor-works.com</div>
  </section>
</main>
</body>
</html>
```